Dog care service needs business card design

Our company is Paws Harbour. We provide care for dogs while their owners are away, either through home visits or a holiday stay in the homes of carefully selected minders. Our existing website & Chatterbook cover should provide all the colour cues for our business cards - namely blues, blondes and grey. We have an existing logo (provided).

www.pawsharbourcare.example.au
www.facebook.com/pawsharbourcareau

We wish to clearly communicate our three areas of service "dog minding, home visits, dog walking".

We would like to have the files ready for upload to Printlyne (or similar) for immediate printing.

Target Market(s)

Dog owners who love their dogs like family

Industry/Entity Type

Business

Contact Information for Business Card

Paws Harbour
Ph: 0417 358 904

Font styles to use
Sans Serif

Colors
33a6d7
3176b5

Requirements
Must have
• Logo
• Telephone number
• website
• "Dog minding, home visits, dog walking"
Should not have
• any additional illustrations beyond the logo.

```html
<!DOCTYPE html>
<html lang="en">
<head>
<meta charset="utf-8">
<title>Paws Harbour – Business Card</title>
<link rel="stylesheet" href="https://fonts.googleapis.com/css2?family=Cabin:wght@400;500;600&display=swap">
<style>
  :root {
    --blue-deep: #3176b5;
    --blue-sky: #33a6d7;
    --ink: #3b3f4a;
    --paper: #ffffff;
    --backdrop: #e4e4e4;
    --logo-tint: #e9f1f9;
  }
  * { box-sizing: border-box; margin: 0; padding: 0; }
  html, body {
    width: 1200px;
    height: 675px;
    overflow: hidden;
    background: var(--backdrop);
    font-family: "Cabin", "Gill Sans", sans-serif;
  }
  .stage {
    position: relative;
    width: 1200px;
    height: 675px;
  }

  /* Card back – portrait, solid blue with logo symbol */
  .card-back {
    position: absolute;
    left: 110px;
    top: 75px;
    width: 300px;
    height: 525px;
    background: var(--blue-deep);
    box-shadow: 0 6px 18px rgba(0,0,0,0.18);
    display: flex;
    align-items: center;
    justify-content: center;
  }
  .card-back__symbol {
    width: 210px;
    height: 250px;
    border-radius: 40px;
    background: linear-gradient(160deg, rgba(255,255,255,0.9), rgba(233,241,249,0.75));
  }

  /* Card front – landscape */
  .card-front {
    position: absolute;
    left: 470px;
    top: 160px;
    width: 620px;
    height: 354px;
    background: var(--paper);
    box-shadow: 0 6px 18px rgba(0,0,0,0.18);
    overflow: hidden;
  }
  .brand {
    position: absolute;
    top: 52px;
    right: 70px;
    display: flex;
    align-items: center;
    gap: 16px;
  }
  .brand__dot {
    width: 54px;
    height: 54px;
    border-radius: 50%;
    background: var(--blue-deep);
  }
  .brand__name {
    font-size: 44px;
    font-weight: 600;
    color: var(--ink);
    letter-spacing: -0.5px;
    line-height: 1;
  }
  .services {
    position: absolute;
    top: 152px;
    left: 52px;
    font-size: 19px;
    font-weight: 500;
    color: var(--ink);
  }
  .rule {
    position: absolute;
    top: 190px;
    left: 0;
    right: 0;
    height: 1.5px;
    background: var(--blue-sky);
  }
  .band {
    position: absolute;
    left: 0;
    width: 515px;
    color: var(--paper);
    display: flex;
    align-items: center;
    padding-left: 40px;
  }
  .band--phone {
    top: 196px;
    height: 52px;
    background: var(--blue-deep);
    font-size: 25px;
  }
  .band--web {
    top: 248px;
    height: 42px;
    background: var(--blue-sky);
    font-size: 22px;
  }
</style>
</head>
<body>
  <main class="stage">
    <section class="card-back">
      <div class="card-back__symbol" role="img" aria-label="Paws Harbour dog logo symbol in white on blue"></div>
    </section>

    <section class="card-front">
      <div class="brand">
        <span class="brand__dot"></span>
        <span class="brand__name">Paws Harbour</span>
      </div>
      <p class="services">Dog minding, home visits, dog walking</p>
      <div class="rule"></div>
      <p class="band band--phone">Paws Harbour Ph: 0417 358 904</p>
      <p class="band band--web">www.pawsharbourcare.example.au</p>
    </section>
  </main>
</body>
</html>
```